Brevin Finance Flyer Design

I would like a high res flyer designed for mass printing. It is for a mortgage and finance broking company in Sydney. We are called Brevin Finance. The wording i would like displayed is the following
Looking For Something Extra from your broker?
Brevin Finance can make all the difference
What we offer you is an extensive range of mortgage and finance products, including:
• Home Loans
• Investment Loans
• Low Doc Loans
• Vehicle Finance
• Equipment Finance
• Commercial Loans
• Refinance
Contact Us
Phone (02) 7354 2816
email info@brevinfinance.com.au
web www.brevinfinance.com.au
Finance

```html
<!DOCTYPE html>
<html lang="en">
<head>
<meta charset="UTF-8">
<title>Brevin Finance Flyer</title>
<link rel="stylesheet" href="https://fonts.googleapis.com/css2?family=Arimo:wght@400;700&family=Open+Sans:wght@400&display=swap">
<style>
  :root {
    --ink: #111111;
    --brand-grey: #4a4a4a;
    --accent-blue: #3b8fd2;
    --footer-bg: #252525;
    --footer-text: #f2f2f2;
    --footer-muted: #dcdcdc;
    --band-grey: #d6d6d6;
    --paper: #ffffff;
  }
  * { margin: 0; padding: 0; box-sizing: border-box; }
  html, body { width: 927px; height: 1200px; overflow: hidden; background: var(--paper); }
  .flyer {
    position: relative; width: 927px; height: 1200px; overflow: hidden;
    background: var(--paper); font-family: "Arimo", Arial, sans-serif; color: var(--ink);
  }
  .hero-photo {
    position: absolute; left: 0; top: 0; width: 927px; height: 308px;
    background: linear-gradient(90deg, #dfe9f2 0%, #eef3f8 35%, #c9d6e4 60%, #3c4f78 78%, #6d7fa3 88%, #e3ebf3 100%);
  }
  .hero-rule {
    position: absolute; left: 0; top: 308px; width: 927px; height: 10px;
    background: linear-gradient(180deg, #c9c9c9, #ececec);
  }
  .brand {
    position: absolute; top: 378px; left: 0; width: 927px; text-align: center;
  }
  .brand-name {
    display: inline-flex; align-items: center; gap: 18px;
    font-family: "Open Sans", Arial, sans-serif; font-weight: 400;
    font-size: 66px; line-height: 1; color: var(--brand-grey);
  }
  .brand-mark { width: 40px; height: 40px; background: var(--brand-grey); }
  .brand-tagline {
    margin-top: 10px; font-family: "Open Sans", Arial, sans-serif;
    font-size: 24px; color: var(--brand-grey); letter-spacing: 0.2px;
  }
  .brand-underline {
    position: absolute; top: 513px; left: 168px; width: 590px; height: 4px;
    background: linear-gradient(90deg, rgba(200,200,200,0), #cfcfcf 50%, rgba(200,200,200,0));
  }
  .headline, .subhead, .intro { position: absolute; left: 0; width: 927px; text-align: center; }
  .headline { top: 548px; font-size: 24.5px; font-weight: 700; }
  .subhead { top: 632px; font-size: 33px; font-weight: 700; }
  .intro { top: 745px; font-size: 21.5px; font-weight: 700; line-height: 35px; }
  .products {
    position: absolute; list-style: none; font-size: 27px; font-weight: 700; line-height: 36px;
  }
  .products li::before {
    content: "•"; color: var(--accent-blue); margin-right: 6px;
  }
  .products-left { left: 64px; top: 850px; }
  .products-right { left: 559px; top: 850px; }
  .footer-rule {
    position: absolute; left: 0; top: 1043px; width: 927px; height: 10px;
    background: linear-gradient(180deg, #bdbdbd, #e4e4e4);
  }
  .contact {
    position: absolute; left: 0; top: 1053px; width: 927px; height: 147px;
    background: var(--footer-bg); text-align: center; color: var(--footer-text);
  }
  .contact-title { margin-top: 16px; font-size: 21px; font-weight: 700; }
  .contact-phone { margin-top: 6px; font-size: 27px; font-weight: 700; letter-spacing: 0.5px; }
  .contact-web { margin-top: 6px; font-size: 21px; color: var(--footer-muted); letter-spacing: 0.4px; }
</style>
</head>
<body>
<div class="flyer">
  <div class="hero-photo" role="img" aria-label="Blurred business people walking through a bright modern office corridor"></div>
  <div class="hero-rule"></div>

  <div class="brand">
    <div class="brand-name"><span class="brand-mark"></span>Brevin Finance</div>
    <div class="brand-tagline">mortgage and finance broking services</div>
  </div>
  <div class="brand-underline"></div>

  <h2 class="headline">Looking For Something Extra from your broker?</h2>
  <h1 class="subhead">Brevin Finance can make all the difference!</h1>
  <p class="intro">What we offer you is an extensive range of mortgage<br>and finance products, including:</p>

  <ul class="products products-left">
    <li>Home Loans</li>
    <li>Investment Loans</li>
    <li>Low Doc Loans</li>
    <li>Vehicle Finance</li>
  </ul>
  <ul class="products products-right">
    <li>Equipment Finance</li>
    <li>Commercial Loans</li>
    <li>Refinance</li>
  </ul>

  <div class="footer-rule"></div>
  <footer class="contact">
    <div class="contact-title">Contact Us</div>
    <div class="contact-phone">Phone (02) 7354 2816</div>
    <div class="contact-web">email: info@brevinfinance.com.au • web www.brevinfinance.com.au</div>
  </footer>
</div>
</body>
</html>
```